Social Media Graphics - ALL TEXT RK

We are looking for a series of social media graphics for Instagram (standard size 1:1 (1080x1080px) that are ALL TEXT. We want the following quotes below on each graphic; one quote per graphic. AND, In very small letters at the bottom of each graphic, add @RKMarlowLive

The look and feel of these graphics should be complimentary to the color palette attached below; but keep them simple. But the design is up to you; at the end of this document, I provided various samples of all text graphics that I like as examples.

Target Market(s)

women looking to lose weight

Industry/Entity Type

health and wellness

Colors
E54698
E96AAD
F1A4CE
F9D9EA
FCEFF6

Requirements
Must have
• the quotes in the document
Should not have
• no stock photography

```html
<!DOCTYPE html>
<html lang="en">
<head>
<meta charset="utf-8">
<title>Overnight Remedy – RK Quote Graphic</title>
<link rel="stylesheet" href="https://fonts.googleapis.com/css2?family=Caveat+Brush&family=Fraunces:ital,opsz,wght@0,9..144,500;0,9..144,600;1,9..144,500;1,9..144,600&family=Montserrat:wght@600;700&display=swap">
<style>
  :root {
    --bg-blush: #fac8e3;
    --ink-pink: #f0147f;
    --ink-magenta: #cf0462;
  }
  html, body {
    margin: 0;
    padding: 0;
    width: 1200px;
    height: 1200px;
    overflow: hidden;
    background: var(--bg-blush);
  }
  .quote-card {
    position: relative;
    width: 1200px;
    height: 1200px;
    background: var(--bg-blush);
    color: var(--ink-pink);
    font-family: "Fraunces", Georgia, serif;
    font-weight: 600;
    font-optical-sizing: none;
    font-variation-settings: "opsz" 9;
  }
  .headline {
    position: absolute;
    left: 72px;
    top: 90px;
    margin: 0;
    font-size: 98px;
    line-height: 102px;
    font-weight: 600;
    letter-spacing: -0.5px;
    white-space: nowrap;
  }
  .headline span { display: block; }
  .yes-word {
    position: absolute;
    left: 370px;
    top: 440px;
    width: 520px;
    height: 420px;
    overflow: visible;
  }
  .yes-word text {
    font-family: "Caveat Brush", "Brush Script MT", cursive;
    fill: var(--ink-magenta);
  }
  .payoff {
    position: absolute;
    right: 80px;
    top: 684px;
    margin: 0;
    font-size: 88px;
    line-height: 89px;
    text-align: right;
    font-weight: 600;
    white-space: nowrap;
  }
  .payoff span { display: block; }
  .payoff em {
    font-style: italic;
    font-weight: 500;
  }
  .handle {
    position: absolute;
    left: 76px;
    top: 1052px;
    margin: 0;
    font-family: "Montserrat", Arial, sans-serif;
    font-weight: 700;
    font-size: 30px;
    letter-spacing: 0.5px;
    text-transform: uppercase;
    color: var(--ink-pink);
    font-variation-settings: normal;
  }
</style>
</head>
<body>
  <main class="quote-card">
    <h1 class="headline">
      <span>Wake up</span>
      <span>tomorrow with</span>
      <span>a flatter belly</span>
    </h1>
    <svg class="yes-word" viewBox="0 0 520 420" aria-label="yes">
      <text x="14" y="250" font-size="330" textLength="490" lengthAdjust="spacingAndGlyphs" transform="rotate(-6 260 210)">yes</text>
    </svg>
    <p class="payoff">
      <span>, this</span>
      <span>overnight</span>
      <span>remedy</span>
      <span>works like</span>
      <span><em>magic</em>!</span>
    </p>
    <p class="handle">@RKMarlowLive</p>
  </main>
</body>
</html>
```